Upmarket Dessert Lounge needs a Business Card Design

We are an upmarket dessert lounge needing a business card to match our image.

We want something that is simple yet beautiful, feminine, classy, sophisticated and elegant. We want it to stand out and don't mind if it is bold.

The design should include our logo and colours of red or maroon with gold highlights. We don't mind if black is used.

Marlow & Quince

Target Market(s)

For those who like to indulge or treat themselves and give in to their temptations on good quality desserts.

Industry/Entity Type

Business

Requirements
Must have
• Must include our logo and our name

Marlow & Quince

M & Q

```html
<!DOCTYPE html>
<html lang="en">
<head>
<meta charset="utf-8">
<title>Marlow &amp; Quince — Business Card</title>
<link rel="stylesheet" href="https://fonts.googleapis.com/css2?family=Cormorant+Garamond:wght@500&family=Italianno&family=Lato:wght@400&display=swap">
<style>
  :root {
    --maroon: #5f151d;
    --maroon-text: #6b1d24;
    --gold: #e8cf92;
    --paper: #ffffff;
    --canvas: #ffffff;
  }
  * { margin: 0; padding: 0; box-sizing: border-box; }
  html, body {
    width: 1200px; height: 900px; overflow: hidden;
    background: var(--canvas);
  }
  .stage { position: relative; width: 1200px; height: 900px; }
  .card {
    position: absolute; top: 112px;
    width: 442px; height: 659px;
    overflow: hidden;
    box-shadow: 0 0 6px rgba(0,0,0,0.12);
  }
  .card--front { left: 88px; background: var(--paper); }
  .card--back { left: 678px; background: var(--maroon); }
  .card__art { position: absolute; inset: 0; width: 442px; height: 659px; }

  .brand-mark {
    position: absolute; left: 52px; top: 68px; width: 150px;
    text-align: center;
    font-family: "Cormorant Garamond", serif; font-weight: 500;
    font-size: 46px; line-height: 60px; color: var(--gold);
  }
  .tagline {
    position: absolute; left: 48px; top: 160px;
    font-family: "Italianno", cursive; color: var(--gold);
    font-size: 50px; line-height: 40px;
  }
  .tagline span { display: block; }
  .tagline span + span { padding-left: 54px; }

  .contact {
    position: absolute; right: 55px; top: 537px;
    text-align: right;
    font-family: "Lato", sans-serif; font-size: 18px;
    line-height: 25px; color: var(--maroon-text);
  }

  .brand-name {
    position: absolute; left: 0; right: 0; top: 484px;
    text-align: center;
    font-family: "Cormorant Garamond", serif; font-weight: 500;
    font-size: 27px; letter-spacing: 0.5px; color: var(--gold);
  }
  .web {
    position: absolute; left: 0; right: 0; top: 588px;
    text-align: center;
    font-family: "Lato", sans-serif; font-size: 20px; color: var(--gold);
  }
</style>
</head>
<body>
<main class="stage">

  <section class="card card--front">
    <svg class="card__art" viewBox="0 0 442 659" aria-hidden="true">
      <defs>
        <radialGradient id="front-flourish-glow" cx="50%" cy="50%" r="50%">
          <stop offset="0%" stop-color="#e8cf92" stop-opacity="0.55"/>
          <stop offset="100%" stop-color="#e8cf92" stop-opacity="0"/>
        </radialGradient>
      </defs>
      <path class="wave-fill" d="M0,0 H365 C335,120 320,260 140,312 C70,332 20,380 0,428 Z" fill="var(--maroon)"/>
      <path class="wave-edge" d="M365,0 C335,120 320,260 140,312 C70,332 20,380 0,428" fill="none" stroke="var(--gold)" stroke-width="3"/>
    </svg>
    <svg class="card__art" viewBox="0 0 442 659" role="img" aria-label="Gold scrolling floral flourish rising along the curve">
      <ellipse cx="230" cy="410" rx="140" ry="120" fill="url(#front-flourish-glow)"/>
      <ellipse cx="360" cy="150" rx="90" ry="140" fill="url(#front-flourish-glow)"/>
    </svg>
    <div class="brand-mark">M &amp; Q</div>
    <p class="tagline"><span>Dessert</span><span>Specialists</span></p>
    <address class="contact" style="font-style:normal">
      Marlow 01632 960142<br>
      Quince 01632 960587<br>
      hello@marlowquince.com
    </address>
  </section>

  <section class="card card--back">
    <svg class="card__art" viewBox="0 0 442 659" aria-hidden="true">
      <defs>
        <radialGradient id="back-flourish-glow" cx="50%" cy="50%" r="50%">
          <stop offset="0%" stop-color="#e8cf92" stop-opacity="0.45"/>
          <stop offset="100%" stop-color="#e8cf92" stop-opacity="0"/>
        </radialGradient>
      </defs>
      <path class="wave-fill" d="M0,0 H250 C270,110 200,170 90,185 C40,192 10,205 0,222 Z" fill="var(--paper)"/>
      <path class="wave-edge" d="M250,0 C270,110 200,170 90,185 C40,192 10,205 0,222" fill="none" stroke="var(--gold)" stroke-width="3"/>
    </svg>
    <svg class="card__art" viewBox="0 0 442 659" role="img" aria-label="Gold scrolling floral flourish spreading from the curve">
      <ellipse cx="140" cy="280" rx="120" ry="95" fill="url(#back-flourish-glow)"/>
      <ellipse cx="260" cy="90" rx="120" ry="80" fill="url(#back-flourish-glow)"/>
    </svg>
    <div class="brand-name">MARLOW &amp; QUINCE</div>
    <div class="web">Marlow-Quince.com</div>
  </section>

</main>
</body>
</html>
```